Cuddle close with the brightest comet in your galaxy Zodiac handbook for finding deep romance and passion

I have had a graphic artist design a book cover which I am perfectly happy with. Unfortunately I've found that she sourced the image from the internet a year ago -- she says that the 90% of the image has been changed, but she hasn't responded to my request to see the original image, unchanged, so that I can be sure. Therefore, it's probably going to be a copyright problem. I have tried to attached the image she has created, which I have in dropbox and my photo library - but the file is huge. Please email me so that I can forward her email and the image on to you at marisolvendt@postvane.com.
Updates

I've had a request to supply a link for dropbox. I have the image in dropbox, but I'm unable to access the link, I'm not sure why. I also have it in iPhoto on my mac. If you are able to supply your email address I can send the iPhoto image to you. Thank you, Marisol Vendt Added Thursday, May 21, 2015

Target Market(s)

Love and sex - mostly women but written for both genders - adult market

Font styles to use
Decorative
Script

Requirements
Must have
• must be original - design must not reproduce, plagiarise or copy another's design. The file attached was submitted by a designer who copied it from the internet and 'cartooned' it so that it would look original, but it doesn't.
Nice to have
• I like the colour scheme in the attached file. the blue and orange text is a good combination, as it the black and white image - I would like a midnight blue background.

```html
<!DOCTYPE html>
<html lang="en">
<head>
<meta charset="utf-8">
<title>Snug Fit — Lulu Marlowe</title>
<link rel="stylesheet" href="https://fonts.googleapis.com/css2?family=Pinyon+Script&family=Poiret+One&family=Playfair+Display&display=swap">
<style>
  :root {
    --paper: #c6cdd2;
    --paper-light: #d8dde0;
    --paper-tint: rgba(70, 90, 150, 0.10);
    --ink: #141414;
    --star-blue: #23336e;
    --brass: #7a6a4c;
    --brass-dark: #4b4030;
    --clip: #8c8f8c;
  }
  html, body {
    margin: 0;
    padding: 0;
    overflow: hidden;
    background: var(--paper);
  }
  .cover {
    position: relative;
    width: 1200px;
    height: 900px;
    overflow: hidden;
    color: var(--ink);
  }
  .cover__texture {
    position: absolute;
    inset: 0;
    background:
      radial-gradient(circle at 18% 30%, var(--paper-tint), transparent 22%),
      radial-gradient(circle at 82% 28%, var(--paper-tint), transparent 24%),
      radial-gradient(circle at 12% 65%, var(--paper-tint), transparent 18%),
      radial-gradient(circle at 88% 66%, var(--paper-tint), transparent 20%),
      radial-gradient(circle at 50% 18%, var(--paper-tint), transparent 26%),
      radial-gradient(ellipse at 50% 45%, var(--paper-light), var(--paper) 78%);
  }
  .cover__text {
    position: absolute;
    left: 0;
    width: 100%;
    margin: 0;
    text-align: center;
    line-height: 1;
    font-weight: 400;
  }
  .author {
    top: 22px;
    font-family: "Pinyon Script", cursive;
    font-size: 86px;
    letter-spacing: 6px;
    -webkit-text-stroke: 1.6px var(--ink);
  }
  .title {
    top: 160px;
    font-family: "Poiret One", sans-serif;
    font-size: 64px;
    letter-spacing: 14px;
  }
  .subtitle {
    top: 232px;
    font-family: "Pinyon Script", cursive;
    font-size: 40px;
    line-height: 44px;
    letter-spacing: 3px;
    -webkit-text-stroke: 0.6px var(--ink);
  }
  .tagline-lead {
    top: 700px;
    font-family: "Pinyon Script", cursive;
    font-size: 50px;
    letter-spacing: 4px;
    -webkit-text-stroke: 0.8px var(--ink);
  }
  .tagline-main {
    top: 756px;
    font-family: "Playfair Display", serif;
    font-size: 42px;
    letter-spacing: 1px;
  }
  .tagline-tail {
    top: 805px;
    font-family: "Pinyon Script", cursive;
    font-size: 36px;
    letter-spacing: 6px;
    -webkit-text-stroke: 0.6px var(--ink);
  }
  .key-photo {
    position: absolute;
    left: 515px;
    top: 335px;
    width: 160px;
    height: 340px;
    border-radius: 50% 50% 40% 40% / 22% 22% 14% 14%;
    background:
      radial-gradient(ellipse at 50% 14%, var(--brass) 0%, var(--brass-dark) 28%, transparent 48%),
      linear-gradient(180deg, transparent 20%, rgba(75, 64, 48, 0.55) 40%, rgba(140, 143, 140, 0.6) 70%, rgba(140, 143, 140, 0.15) 100%);
  }
  .symbol {
    position: absolute;
    overflow: visible;
  }
  .symbol path,
  .symbol circle {
    fill: none;
    stroke: var(--star-blue);
    stroke-width: 4;
    stroke-linecap: round;
  }
</style>
</head>
<body>
  <main class="cover">
    <div class="cover__texture" role="img" aria-label="Pale grey paper texture scattered with small hand-drawn blue stars"></div>

    <h2 class="cover__text author">Lulu Marlowe</h2>
    <h1 class="cover__text title">SNUG FIT</h1>
    <p class="cover__text subtitle">Cuddle close with the brightest comet in your<br>galaxy</p>

    <svg class="symbol" style="left:250px;top:515px" width="130" height="105" viewBox="0 0 130 105" aria-label="Female symbol" role="img">
      <circle cx="48" cy="32" r="30"/>
      <path d="M68 55 L112 98 M78 90 L108 70"/>
    </svg>
    <svg class="symbol" style="left:785px;top:540px" width="160" height="85" viewBox="0 0 160 85" aria-label="Male symbol" role="img">
      <circle cx="45" cy="52" r="30"/>
      <path d="M72 38 L145 14 M118 8 L146 14 L134 36"/>
    </svg>

    <div class="key-photo" role="img" aria-label="Photograph of an ornate brass key charm with a small heart, hooked on a paperclip"></div>

    <p class="cover__text tagline-lead">Zodiac handbook for</p>
    <p class="cover__text tagline-main">FINDING DEEP</p>
    <p class="cover__text tagline-tail">romance and passion</p>
  </main>
</body>
</html>
```